Copperfox Billboard

Please design a billboard using my photos and logos.
For photo of truck please crop the truck itself out and not have the trees / dirt in photo.
Please put " Best Prices in Sevier County"
Please put " 30-yard Dumpsters Starting at 600.00"
Please put " 16-yard Dumpsters Starting at 300.0"
Please put " Delivery and Pickup 7 Days a week"
Billboard size will be 10 ft tall 30 ft wide

```html
<!DOCTYPE html>
<html lang="en">
<head>
<meta charset="utf-8">
<title>Copperfox Dumpsters Billboard</title>
<link href="https://fonts.googleapis.com/css2?family=Arimo:wght@700&display=swap" rel="stylesheet">
<style>
  :root {
    --page-bg: #e8e8ec;
    --board-purple: #52266b;
    --headline-yellow: #f4cf1d;
    --card-white: #ffffff;
    --ink-black: #111111;
    --band-black: #0c0c0c;
    --photo-light: #e9e9ec;
    --photo-dark: #2e1a5c;
  }
  * { margin: 0; padding: 0; box-sizing: border-box; }
  html, body {
    width: 1200px;
    height: 655px;
    overflow: hidden;
    background: var(--page-bg);
  }
  .board {
    position: absolute;
    left: 0;
    top: 108px;
    width: 1200px;
    height: 439px;
    background: var(--board-purple);
    font-family: "Arimo", Arial, sans-serif;
    font-weight: 700;
    overflow: hidden;
  }
  .brand {
    position: absolute;
    left: 95px;
    top: 40px;
    width: 352px;
    text-align: center;
    color: var(--card-white);
    line-height: 1;
  }
  .brand-name {
    display: block;
    font-size: 62px;
    letter-spacing: 1px;
    text-transform: uppercase;
  }
  .brand-tag {
    display: block;
    margin-top: 6px;
    font-size: 34px;
    letter-spacing: 1px;
    text-transform: uppercase;
  }
  .headline {
    position: absolute;
    left: 60px;
    top: 178px;
    width: 426px;
    text-align: center;
    color: var(--headline-yellow);
    font-size: 42px;
    line-height: 1.05;
    text-transform: uppercase;
  }
  .price-card {
    position: absolute;
    top: 274px;
    width: 170px;
    height: 117px;
    background: var(--card-white);
    border-radius: 12px;
    color: var(--ink-black);
    text-align: center;
    text-transform: uppercase;
  }
  .price-card--30 { left: 90px; }
  .price-card--16 { left: 286px; }
  .price-card__label {
    padding-top: 8px;
    font-size: 18px;
    line-height: 1.3;
  }
  .price-card__rule {
    height: 2px;
    background: var(--ink-black);
    margin: 4px 0 0;
  }
  .price-card__amount {
    font-size: 18px;
    padding-top: 10px;
  }
  .truck-photo {
    position: absolute;
    left: 509px;
    top: 27px;
    width: 654px;
    height: 379px;
  }
  .service-band {
    position: absolute;
    left: 768px;
    top: 291px;
    width: 430px;
    height: 90px;
    background: var(--band-black);
    color: var(--headline-yellow);
    font-size: 28px;
    line-height: 1.2;
    text-align: center;
    text-transform: uppercase;
    display: flex;
    flex-direction: column;
    justify-content: center;
  }
</style>
</head>
<body>
  <main class="board">
    <div class="brand">
      <span class="brand-name">Copperfox</span>
      <span class="brand-tag">Dumpsters</span>
    </div>

    <h1 class="headline">Best Prices in<br>Sevier County</h1>

    <div class="price-card price-card--30">
      <p class="price-card__label">30 - Yard<br>Dumpsters<br>Starting at</p>
      <div class="price-card__rule"></div>
      <p class="price-card__amount">600.00 $</p>
    </div>

    <div class="price-card price-card--16">
      <p class="price-card__label">16 - Yard<br>Dumpsters<br>Starting at</p>
      <div class="price-card__rule"></div>
      <p class="price-card__amount">300.00 $</p>
    </div>

    <svg class="truck-photo" viewBox="0 0 654 379" role="img" aria-label="Cut-out photo of a white roll-off truck carrying a purple dumpster container">
      <defs>
        <linearGradient id="truckTone" x1="0" y1="0" x2="1" y2="0">
          <stop offset="0" stop-color="var(--photo-light)"/>
          <stop offset="0.55" stop-color="#cfcfd6"/>
          <stop offset="1" stop-color="var(--photo-dark)"/>
        </linearGradient>
      </defs>
      <rect x="0" y="0" width="654" height="379" rx="24" fill="url(#truckTone)"/>
    </svg>

    <div class="service-band">
      <span>Delivery and Pickup</span>
      <span>7 Days a Week</span>
    </div>
  </main>
</body>
</html>
```